Tallowreed Advisory Partners Business Card Design

We have the logo we just need someone to design a modern business card design.

Name: Desmond Munkalt
Phone: 3055550148
Mobile: 9175550193
Web:www.tallowreedadvisory.example
email: dmunkalt@tallowreedadvisory.example
Company: Tallowreed Advisory Partners
Title: CEO

Address: 718 Quillmore Ave, Miami, Florida 33190

Target Market(s)

companies over 100 employees

Industry/Entity Type

Business

```html
<!DOCTYPE html>
<html lang="en">
<head>
<meta charset="utf-8">
<title>Tallowreed Advisory Partners – Business Card</title>
<link rel="stylesheet" href="https://fonts.googleapis.com/css2?family=Lato:wght@400;700;900&display=swap">
<style>
  :root {
    --bg: #e9ebef;
    --blue: #0b5ff0;
    --blue-deep: #1746d2;
    --navy: #0d2a7a;
    --ink: #111111;
    --text: #222222;
    --white: #ffffff;
    --divider: #2f6ff0;
  }
  * { box-sizing: border-box; margin: 0; padding: 0; }
  html, body { width: 1200px; height: 900px; overflow: hidden; }
  body { background: var(--bg); font-family: "Lato", sans-serif; position: relative; }

  .card {
    position: absolute;
    width: 600px;
    height: 343px;
    border-radius: 2px;
    box-shadow: 0 10px 30px rgba(0,0,0,0.18);
    overflow: hidden;
  }

  /* Front */
  .card-front {
    left: 60px; top: 60px;
    background: linear-gradient(135deg, var(--blue) 0%, var(--blue-deep) 100%);
  }
  .front-circle {
    position: absolute;
    left: 200px; top: 70px;
    width: 200px; height: 200px;
    border-radius: 50%;
    background: rgba(255,255,255,0.08);
  }
  .front-name {
    position: absolute;
    left: 0; right: 0; top: 140px;
    text-align: center;
    color: var(--white);
    font-size: 30px;
    font-weight: 400;
    letter-spacing: 0.3px;
  }
  .front-tagline {
    position: absolute;
    left: 0; right: 0; top: 184px;
    text-align: center;
    color: var(--navy);
    font-size: 15px;
    letter-spacing: 1px;
  }

  /* Back */
  .card-back {
    left: 540px; top: 497px;
    background: linear-gradient(160deg, #ffffff 0%, #f1f2f4 100%);
    display: flex;
  }
  .brand {
    width: 290px;
    display: flex;
    flex-direction: column;
    align-items: center;
    justify-content: center;
    gap: 14px;
  }
  .brand-dot {
    width: 62px; height: 62px;
    border-radius: 50%;
    background: var(--blue);
  }
  .brand-name {
    color: var(--ink);
    font-weight: 900;
    font-size: 21px;
    line-height: 1.15;
    text-align: center;
    text-transform: uppercase;
    letter-spacing: 0.5px;
  }
  .divider {
    width: 2px;
    margin: 36px 0;
    background: linear-gradient(to bottom, transparent, var(--divider) 30%, var(--divider) 70%, transparent);
  }
  .details {
    flex: 1;
    padding: 52px 0 0 30px;
    color: var(--text);
  }
  .person-name { color: var(--blue); font-size: 20px; font-weight: 400; }
  .person-title { color: var(--blue); font-size: 15px; margin: 2px 0 0 10px; }
  .address { font-size: 13.5px; margin: 14px 0 14px 10px; }
  .contact-list { list-style: none; margin-left: 10px; }
  .contact-list li {
    display: flex; align-items: center; gap: 10px;
    font-size: 14px; height: 24px;
  }
  .contact-list svg { width: 15px; height: 15px; fill: var(--blue); flex: none; }
</style>
</head>
<body>

<section class="card card-front">
  <div class="front-circle"></div>
  <h1 class="front-name">Tallowreed Advisory Partners</h1>
  <p class="front-tagline">companies over 100 employees</p>
</section>

<section class="card card-back">
  <div class="brand">
    <div class="brand-dot"></div>
    <div class="brand-name">Tallowreed<br>Advisory Partners</div>
  </div>
  <div class="divider"></div>
  <div class="details">
    <h2 class="person-name">Desmond Munkalt</h2>
    <p class="person-title">CEO</p>
    <p class="address">718 Quillmore Ave, Miami, Florida 33190</p>
    <ul class="contact-list">
      <li>
        <svg viewBox="0 0 16 16" aria-hidden="true"><path d="M2 5c0-2 2-3 6-3s6 1 6 3v1h-3V5H5v1H2zM4 7h8l2 6H2z"/></svg>
        3055550148
      </li>
      <li>
        <svg viewBox="0 0 16 16" aria-hidden="true"><path d="M4 1h8v14H4zM5.5 3v8h5V3zM7 12.5h2v1H7z" fill-rule="evenodd"/></svg>
        9175550193
      </li>
      <li>
        <svg viewBox="0 0 16 16" aria-hidden="true"><path d="M1 3h14v10H1zM2 4l6 5 6-5v-.2H2z"/></svg>
        dmunkalt@tallowreedadvisory.example
      </li>
      <li>
        <svg viewBox="0 0 16 16" aria-hidden="true"><circle cx="8" cy="8" r="7"/><path d="M1 8h14M8 1c3 3 3 11 0 14M8 1c-3 3-3 11 0 14" stroke="#fff" stroke-width="1" fill="none"/></svg>
        www.tallowreedadvisory.example
      </li>
    </ul>
  </div>
</section>

</body>
</html>
```